Willowbrook Haven tri-fold brochure

We are a small assisted living in a home-like environment. Brochure should be warm, heartfelt and include the list of services we provide (see existing brochure). I also want the front picture replaced with stock photo (so no picture of owners). New name to use (instead of Trina) is Dorian Kellsey, and email is kellsey@fernmail.test. Address is same. If you can find better photos, that would be good, all the photos here are dated. We are looking for a more professional design that still conveys warmth, because we are in a home-setting and only care for 9 residents.

Target Market(s)

35-55 year old children looking for an assisted living because their parents are unable to care for them.

Industry/Entity Type

Environment

Contact Information for Business Card

Dorian Kellsey
Willowbrook Haven or Willowbrook Haven Assisted Living
18372 Pinegrove Ln. Conroe, TX 77384
281-555-0187

Requirements
Must have
• List of services offered (feel free to re-word or add/change)
• Be sure to change "Trina/Treena" to Dorian / Dorian Kellsey

```html
<!DOCTYPE html>
<html lang="en">
<head>
<meta charset="utf-8">
<title>Willowbrook Haven – Brochure Inside Panels</title>
<link rel="stylesheet" href="https://fonts.googleapis.com/css2?family=Work+Sans:wght@300;400;700&display=swap">
<style>
  :root {
    --cream: #eee2d8;
    --clay: #b68d6b;
    --heading: #5b2a0f;
    --ink: #2a1f18;
    --photo-walk: #8a9a72;
    --photo-reading: #9c8570;
    --photo-companion: #7a5238;
  }
  * { margin: 0; padding: 0; box-sizing: border-box; }
  html, body { width: 1200px; height: 927px; overflow: hidden; }
  body { font-family: "Work Sans", Helvetica, Arial, sans-serif; color: var(--ink); background: var(--cream); }
  .spread { position: relative; width: 1200px; height: 927px; overflow: hidden; background: var(--cream); }
  .backdrop { position: absolute; inset: 0; }
  .panel { position: absolute; top: 0; text-align: center; }
  .panel-why { left: 10px; width: 380px; }
  .panel-home { left: 810px; width: 380px; }
  .heading { color: var(--heading); font-weight: 700; line-height: 1.05; letter-spacing: -0.2px; }
  .panel-why .heading { font-size: 28px; margin-top: 22px; margin-bottom: 2px; }
  .panel-home .heading { font-size: 31px; line-height: 31px; margin-top: 26px; margin-bottom: 6px; }
  .body-copy { font-weight: 300; font-size: 24px; line-height: 30.4px; }
  .panel-why .body-copy + .body-copy { margin-top: 30.4px; }
  .panel-home .body-copy { font-size: 22px; line-height: 28.8px; }
  .panel-home .body-copy + .body-copy { margin-top: 28.8px; }
  .photo { position: absolute; border-radius: 4px; }
  .photo-reading { left: 29px; top: 666px; width: 341px; height: 232px; background: var(--photo-reading); }
  .photo-walk { left: 430px; top: 32px; width: 340px; height: 236px; background: var(--photo-walk); }
  .photo-companion { left: 830px; top: 632px; width: 342px; height: 262px; background: var(--photo-companion); }
  .services-title { position: absolute; left: 426px; width: 348px; top: 279px; font-size: 32px; text-align: center; }
  .services-list { position: absolute; left: 428px; top: 322px; width: 344px; list-style: none; text-align: justify; }
  .services-list li {
    position: relative; padding-left: 26px; font-weight: 300;
    font-size: 19px; line-height: 24.2px; margin-bottom: 24.2px;
  }
  .services-list li::before {
    content: ""; position: absolute; left: 3px; top: 9px;
    width: 7px; height: 7px; border-radius: 50%; background: var(--ink);
  }
</style>
</head>
<body>
<main class="spread">
  <svg class="backdrop" width="1200" height="927" viewBox="0 0 1200 927" aria-hidden="true">
    <defs>
      <filter id="soften" x="-10%" y="-10%" width="120%" height="120%">
        <feGaussianBlur stdDeviation="28"/>
      </filter>
      <linearGradient id="clayFade" x1="0" y1="0" x2="0" y2="1">
        <stop offset="0" stop-color="#c09a79"/>
        <stop offset="1" stop-color="#b5896a"/>
      </linearGradient>
    </defs>
    <rect width="1200" height="927" fill="#eee2d8"/>
    <path d="M-60,470 C160,440 420,300 600,350 C760,395 900,560 1260,640 L1260,990 L-60,990 Z"
          fill="url(#clayFade)" filter="url(#soften)"/>
  </svg>

  <section class="panel panel-why">
    <h2 class="heading">Why Willowbrook Haven?</h2>
    <p class="body-copy">Choosing the right place<br>for your loved one is an<br>important decision.<br>Willowbrook Haven is here to<br>help give you peace of mind.</p>
    <p class="body-copy">Innovative care in a<br>residential environment<br>provides a wonderful<br>alternative to institutional<br>living. Our residents truly<br>become a family because of<br>the small, intimate, home-like<br>atmosphere.</p>
    <p class="body-copy">Our first concern is make<br>life safe, comfortable and<br>enjoyable for those who have<br>been entrusted to us.</p>
  </section>
  <div class="photo photo-reading" role="img" aria-label="Photo of an older couple reading together on a sofa"></div>

  <div class="photo photo-walk" role="img" aria-label="Photo of a caregiver walking outdoors with a resident using a walker"></div>
  <h2 class="heading services-title">Services</h2>
  <ul class="services-list">
    <li>Medical supervision provided by visiting physicians and nursing personnel.</li>
    <li>Rehabilitation, home health and hospice services available through licensed professionals.</li>
    <li>Medications and incontinence management.</li>
    <li>Personal attention, caregiver involvement and heightened activities focusing on hobbies, crafts, exercise, music therapy, holiday and birthday celebrations and plant and pet therapy.</li>
    <li>Nutritious home cooked meals and snacks with emphasis on hydration.</li>
    <li>Assistance with bathing, grooming and other personal needs including daily laundry and housekeeping.</li>
  </ul>

  <section class="panel panel-home">
    <h2 class="heading">Willowbrook Haven is<br>YOUR HOME</h2>
    <p class="body-copy">The comforts of home in a<br>private luxurious setting allows<br>loving care with dignity.</p>
    <p class="body-copy">Private or companion<br>rooms, elegantly furnished or<br>personalized to your style.</p>
    <p class="body-copy">A living room, family room,<br>dining room, sun room and<br>kitchen residents can call their<br>own so they can live the way<br>they always have.</p>
    <p class="body-copy">Enjoy beautiful days on the<br>patio and in the lovely garden<br>area with beautiful trees,<br>flowers and birds.</p>
  </section>
  <div class="photo photo-companion" role="img" aria-label="Photo of a smiling resident holding a small dog"></div>
</main>
</body>
</html>
```